Global Business News and Stock Market News website

I am into journalism and a blogger. I want to change and design an entirely new website which will deal strictly on business news and stock market reports from top and leading economies around the world such as US, UK, GERMANY, FRANCE, CHINA, JAPAN, etc. For instance, the UK have opted to leave the EU. The target of my website are business news enthusiasts and investors. My website is to be professionally designed. I would like a layout of blue and green colors. The imagery of my website will include photos of stocks markets index. Designers can get inspiration from http://qorvanbrief.com

Industry/Entity Type

Business

Coding

Coded - Design and coding required

```html
<!DOCTYPE html>
<html lang="en">
<head>
<meta charset="utf-8">
<title>Qorvan Brief — Business &amp; Market News</title>
<link rel="stylesheet" href="https://fonts.googleapis.com/css2?family=Oswald:wght@400;500&family=Roboto:wght@400;500;700&display=swap">
<style>
:root{
  --blue:#2b8fd6;
  --blue-dark:#1f6fae;
  --green:#35b47a;
  --green-dark:#2a9866;
  --ink:#333;
  --muted:#8a8a8a;
  --line:#e3e3e3;
  --page:#f0f0f0;
  --panel:#fff;
  --topbar:#1c1c1c;
  --footer-base:#1f1f1f;
  --orange:#f0a030;
  --sky:#3fb0e8;
  --navy:#3b5b98;
  --signup:#c0392b;
}
*{box-sizing:border-box;margin:0;padding:0}
html,body{width:1200px;height:2584px;overflow:hidden}
body{background:var(--page);font-family:"Roboto",sans-serif;color:var(--ink);position:relative;font-size:13px}
.abs{position:absolute}
.topbar{left:0;top:0;width:1200px;height:26px;background:var(--topbar);color:#bbb;font-size:9px;display:flex;align-items:center;justify-content:space-between;padding:0 20px;letter-spacing:.3px}
.topbar span b{color:#fff;font-weight:500}
.topbar .up{color:var(--green)}
.topbar .down{color:#e06060}
.header{left:88px;top:26px;width:1024px;height:100px;display:flex;align-items:center;justify-content:space-between}
.logo{font-family:"Oswald",sans-serif;font-weight:500;font-size:34px;color:var(--blue);letter-spacing:1px;display:flex;align-items:center;gap:12px}
.logo i{width:14px;height:14px;background:var(--green);display:block}
.header-tools{display:flex;align-items:center;gap:18px;font-size:12px;font-weight:500}
.search{width:180px;height:30px;border:1px solid #ccc;background:#fff;display:flex;align-items:center;justify-content:space-between;padding:0 10px;color:#aaa;font-size:11px}
.nav{left:88px;top:128px;width:1024px;height:42px;background:var(--blue);display:flex}
.nav a{color:#fff;text-decoration:none;font-family:"Oswald",sans-serif;font-size:13px;padding:0 18px;display:flex;align-items:center;letter-spacing:.4px}
.nav a.active{background:var(--green)}
.hero{left:88px;top:176px;width:1024px;height:504px;background:linear-gradient(135deg,#c9d2d8 0%,#7d8a94 40%,#3a4550 75%,#222b33 100%)}
.hero-caption{position:absolute;left:0;bottom:0;width:100%;height:56px;background:rgba(0,0,0,.55);display:flex;align-items:center;justify-content:space-between;padding:0 20px}
.hero-caption h1{font-family:"Oswald",sans-serif;font-weight:400;color:#fff;font-size:22px;letter-spacing:.5px}
.arrows{display:flex;gap:4px}
.arrows span{width:22px;height:22px;background:rgba(255,255,255,.25);display:flex;align-items:center;justify-content:center}
.sec-title{font-family:"Oswald",sans-serif;font-weight:500;color:var(--blue);font-size:16px;letter-spacing:.5px;display:flex;align-items:center;gap:12px}
.sec-title::after{content:"";flex:1;height:1px;background:#cfcfcf}
.panel{background:var(--panel);box-shadow:0 1px 2px rgba(0,0,0,.08)}
.photo{position:relative;overflow:hidden}
.rating{position:absolute;top:12px;right:12px;width:60px;height:60px;background:var(--green);color:#fff;text-align:center;font-family:"Oswald",sans-serif;font-size:22px;line-height:1;padding-top:10px}
.rating small{display:block;font-family:"Roboto",sans-serif;font-size:9px;margin-top:4px}
.overlay-title{position:absolute;left:0;bottom:0;width:100%;padding:10px 14px;background:linear-gradient(transparent,rgba(0,0,0,.7));color:#fff;font-size:14px}
.meta{display:flex;justify-content:space-between;align-items:center;font-size:10px;color:var(--muted);padding:10px 4px}
.meta .icons{display:flex;gap:8px}
.meta .icons i{width:10px;height:10px;background:#bbb;display:block;border-radius:2px}
.latest{left:88px;top:752px;width:692px;height:636px;padding:22px;display:grid;grid-template-columns:1fr 1fr;gap:18px 24px}
.latest .card .photo{height:246px}
.popular{left:800px;top:752px;width:312px;height:636px;padding:14px 14px}
.pop-item{display:flex;gap:12px;padding:9px 0;border-bottom:1px solid var(--line)}
.pop-item:last-child{border-bottom:0}
.pop-item .thumb{width:70px;height:52px;flex:none}
.pop-item p{font-size:12px;line-height:1.45;color:#444}
.biz{left:88px;top:1488px;width:692px;height:256px;padding:22px;display:grid;grid-template-columns:repeat(3,1fr);gap:24px}
.biz .photo{height:140px}
.biz p{font-size:12px;line-height:1.45;margin-top:12px;color:#444}
.biz .date{font-size:10px;color:var(--muted);margin-top:8px}
.dots{display:flex;gap:4px;align-items:center}
.dots i{width:6px;height:6px;border-radius:50%;background:#bbb;display:block}
.dots i.on{background:var(--blue)}
.stock{left:800px;top:1488px;width:312px;height:280px;padding:14px}
.stock .photo{height:216px}
.econ{left:88px;top:1864px;width:692px;height:360px;padding:22px;display:flex;gap:22px}
.econ .big{width:310px;flex:none}
.econ .big .photo{height:272px}
.econ-list{flex:1}
.econ-item{display:flex;gap:14px;padding:6px 0 10px}
.econ-item .thumb{width:96px;height:66px;flex:none}
.econ-item p{font-size:12px;line-height:1.45;color:#444}
.tags{left:800px;top:1864px;width:312px;height:190px;padding:18px;display:flex;flex-wrap:wrap;gap:8px;align-content:flex-start}
.tag{background:#e9e9e9;font-size:11px;padding:7px 12px;color:#555}
.tag.on{background:var(--green);color:#fff}
.social{left:800px;top:2070px;width:312px;height:154px;display:flex;gap:10px}
.social div{flex:1;color:#fff;display:flex;flex-direction:column;align-items:center;justify-content:center;gap:6px;font-size:11px;text-align:center;line-height:1.3}
.social i{width:22px;height:22px;border-radius:50%;background:rgba(255,255,255,.9);display:block}
.s1{background:var(--navy)}.s2{background:var(--sky)}.s3{background:var(--orange)}
.footer{left:0;top:2264px;width:1200px;height:270px;background:var(--green);color:#fff}
.footer-inner{width:1024px;margin:0 auto;padding-top:34px;display:grid;grid-template-columns:repeat(4,1fr);gap:28px}
.footer h4{font-family:"Oswald",sans-serif;font-weight:400;font-size:15px;letter-spacing:.5px;margin-bottom:16px}
.footer p{font-size:11px;line-height:1.6;color:#e8fff3}
.email-field{margin-top:12px;width:200px;height:28px;background:#fff;color:#aaa;font-size:11px;padding:7px 10px}
.btn{margin-top:10px;display:inline-block;background:var(--signup);color:#fff;font-size:11px;font-weight:500;padding:7px 16px}
.follow li{list-style:none;display:flex;align-items:center;gap:10px;font-size:12px;margin-bottom:12px}
.follow i{width:20px;height:20px;border-radius:50%;background:rgba(255,255,255,.9);display:block}
.copyright{left:0;top:2534px;width:1200px;height:50px;background:var(--footer-base);color:#aaa;font-size:11px;display:flex;align-items:center;justify-content:center}
.ph-blue{background:linear-gradient(135deg,#b8cfe0,#5a7d99)}
.ph-gray{background:linear-gradient(135deg,#d8dcdf,#7c858c)}
.ph-dark{background:linear-gradient(135deg,#4e6478,#1c2733)}
.ph-green{background:linear-gradient(135deg,#cfe4d2,#6f9a7a)}
.ph-warm{background:linear-gradient(135deg,#e2d3bf,#8d7a62)}
</style>
</head>
<body>

<div class="abs topbar">
  <span><b>INDEX A</b> 18,240.12 <span class="up">+0.34%</span></span>
  <span><b>INDEX B</b> 6,504.33 <span class="down">-0.12%</span></span>
  <span><b>INDEX C</b> 10,412.80 <span class="up">+0.58%</span></span>
  <span><b>INDEX D</b> 4,322.19 <span class="up">+0.21%</span></span>
  <span><b>INDEX E</b> 16,885.44 <span class="down">-0.47%</span></span>
  <span><b>INDEX F</b> 2,971.06 <span class="up">+0.09%</span></span>
</div>

<header class="abs header">
  <div class="logo"><i></i>QORVAN BRIEF</div>
  <div class="header-tools">
    <div class="search">Search
      <svg width="12" height="12" viewBox="0 0 12 12"><circle cx="5" cy="5" r="4" fill="none" stroke="#999" stroke-width="1.5"/><line x1="8" y1="8" x2="11" y2="11" stroke="#999" stroke-width="1.5"/></svg>
    </div>
    <span>LOGIN / REGISTER</span>
  </div>
</header>

<nav class="abs nav">
  <a class="active">HOME</a><a>WORLD</a><a>POLITICS</a><a>ECONOMY</a><a>BUSINESS</a><a>TECH</a><a>MARKETS</a><a>OPINION</a><a>ARTS</a><a>LIFE</a><a>REAL ESTATE</a>
</nav>

<section class="abs hero" role="img" aria-label="Photo of hands working on a laptop showing market charts">
  <div class="hero-caption">
    <h1>NEQUE PORRO QUISQUAM EST QUI DOLOREM IPSUM</h1>
    <div class="arrows">
      <span><svg width="8" height="10"><path d="M7 1 2 5l5 4" fill="none" stroke="#fff" stroke-width="1.6"/></svg></span>
      <span><svg width="8" height="10"><path d="M1 1l5 4-5 4" fill="none" stroke="#fff" stroke-width="1.6"/></svg></span>
    </div>
  </div>
</section>

<h2 class="abs sec-title" style="left:88px;top:716px;width:692px">LATEST POSTS</h2>
<h2 class="abs sec-title" style="left:800px;top:716px;width:312px">POPULAR POSTS</h2>

<section class="abs panel latest">
  <article class="card">
    <div class="photo ph-gray" role="img" aria-label="Photo of business people in a meeting">
      <div class="rating">8.7<small>Rating</small></div>
      <div class="overlay-title">Neque porro quisquam est</div>
    </div>
    <div class="meta"><span>Business</span><span class="icons"><i></i><i></i><i></i></span></div>
  </article>
  <article class="card">
    <div class="photo ph-green" role="img" aria-label="Photo of a businessman with a growing plant">
      <div class="overlay-title">Neque porro quisquam est</div>
    </div>
    <div class="meta"><span>Markets</span><span class="icons"><i></i><i></i><i></i></span></div>
  </article>
  <article class="card">
    <div class="photo ph-blue" role="img" aria-label="Illustration of finance charts with rising arrows">
      <div class="overlay-title">Neque porro quisquam est</div>
    </div>
    <div class="meta"><span>Economy</span><span class="icons"><i></i><i></i><i></i></span></div>
  </article>
  <article class="card">
    <div class="photo ph-dark" role="img" aria-label="Photo of an investment chart on a screen">
      <div class="rating">10<small>Rating</small></div>
      <div class="overlay-title">Neque porro quisquam est</div>
    </div>
    <div class="meta"><span>Investment</span><span class="icons"><i></i><i></i><i></i></span></div>
  </article>
</section>

<aside class="abs panel popular">
  <div class="pop-item"><div class="thumb ph-gray" role="img" aria-label="Market thumbnail photo"></div><p>Ipsum is simply dummy text of the printing and type</p></div>
  <div class="pop-item"><div class="thumb ph-blue" role="img" aria-label="Market thumbnail photo"></div><p>Ipsum is simply dummy text of the printing and type</p></div>
  <div class="pop-item"><div class="thumb ph-dark" role="img" aria-label="Market thumbnail photo"></div><p>Ipsum is simply dummy text of the printing and type</p></div>
  <div class="pop-item"><div class="thumb ph-green" role="img" aria-label="Market thumbnail photo"></div><p>Ipsum is simply dummy text of the printing and type</p></div>
  <div class="pop-item"><div class="thumb ph-warm" role="img" aria-label="Market thumbnail photo"></div><p>Ipsum is simply dummy text of the printing and type</p></div>
  <div class="pop-item"><div class="thumb ph-blue" role="img" aria-label="Market thumbnail photo"></div><p>Ipsum is simply dummy text of the printing and type</p></div>
  <div class="pop-item"><div class="thumb ph-gray" role="img" aria-label="Market thumbnail photo"></div><p>Ipsum is simply dummy text of the printing and type</p></div>
  <div class="pop-item"><div class="thumb ph-warm" role="img" aria-label="Market thumbnail photo"></div><p>Ipsum is simply dummy text of the printing and type</p></div>
</aside>

<h2 class="abs sec-title" style="left:88px;top:1452px;width:630px">BUSINESS NEWS</h2>
<div class="abs dots" style="left:732px;top:1461px"><i class="on"></i><i></i><i></i></div>
<h2 class="abs sec-title" style="left:800px;top:1452px;width:280px">STOCK MARKET</h2>
<div class="abs dots" style="left:1090px;top:1461px"><i></i><i></i></div>

<section class="abs panel biz">
  <article><div class="photo ph-blue" role="img" aria-label="Photo of a growth chart on paper"></div><p>Ipsum is simply dummy text of the printing and type</p><div class="date">27 March 2016</div></article>
  <article><div class="photo ph-gray" role="img" aria-label="Photo of a business team"></div><p>Ipsum is simply dummy text of the printing and type</p><div class="date">7 March 2016</div></article>
  <article><div class="photo ph-green" role="img" aria-label="Photo of rising bar chart"></div><p>Ipsum is simply dummy text of the printing and type</p><div class="date">1 January 2016</div></article>
</section>

<aside class="abs panel stock">
  <div class="photo ph-dark" role="img" aria-label="Photo of a trader in front of market data">
    <div class="overlay-title">Porro quisquam est, qui</div>
  </div>
  <div class="meta"><span>Photographs</span><span class="icons"><i></i><i></i></span></div>
</aside>

<h2 class="abs sec-title" style="left:88px;top:1828px;width:692px">ECONOMIES</h2>
<h2 class="abs sec-title" style="left:800px;top:1828px;width:312px">Tags</h2>

<section class="abs panel econ">
  <article class="big">
    <div class="photo ph-dark" role="img" aria-label="Photo of a person working on a laptop">
      <div class="rating">8.7<small>Rating</small></div>
      <div class="overlay-title">Interview with mira castellan</div>
    </div>
    <div class="meta"><span>Interviews</span><span class="icons"><i></i><i></i><i></i></span></div>
  </article>
  <div class="econ-list">
    <div class="econ-item"><div class="thumb ph-gray" role="img" aria-label="Economy thumbnail photo"></div><p>Ipsum is simply dummy text of the printing and type</p></div>
    <div class="econ-item"><div class="thumb ph-warm" role="img" aria-label="Economy thumbnail photo"></div><p>Lorem ipsum has been the standard dummy text ever since the early days of print</p></div>
    <div class="econ-item"><div class="thumb ph-blue" role="img" aria-label="Economy thumbnail photo"></div><p>Ipsum is simply dummy text of the printing and type</p></div>
    <div class="econ-item"><div class="thumb ph-green" role="img" aria-label="Economy thumbnail photo"></div><p>Ipsum is simply dummy text of the printing and type</p></div>
  </div>
</section>

<aside class="abs panel tags">
  <span class="tag">developer</span><span class="tag">business</span>
  <span class="tag">themehall</span><span class="tag">pagecraft themes</span>
  <span class="tag">option</span><span class="tag">portfolio concept</span>
  <span class="tag on">markets</span><span class="tag">pagecraft plugins</span>
  <span class="tag">magazine template</span>
</aside>

<div class="abs social">
  <div class="s1"><i></i>698<br>Fans</div>
  <div class="s2"><i></i>698<br>Followers</div>
  <div class="s3"><i></i>698<br>Subscribers</div>
</div>

<footer class="abs footer">
  <div class="footer-inner">
    <div>
      <h4>NEWSLETTERS SIGN UP</h4>
      <p>Sign up for our daily briefing on markets and world economies.</p>
      <div class="email-field">Email address</div>
      <span class="btn">SUBSCRIBE</span>
    </div>
    <div>
      <h4>QUISQUAM EST QUI</h4>
      <p>Lorem ipsum has been the industry's standard dummy text ever since the early days, when an unknown printer took a galley.</p>
      <p style="margin-top:10px">It has survived not only five centuries but also the leap into electronic type.</p>
    </div>
    <div>
      <h4>GET IN TOUCH</h4>
      <p>Address : 17 Harbour Lane, Fenwick</p>
      <p>Phone : +1 555 0142 88</p>
      <p>Email : desk@qorvanbrief.com</p>
      <p>Web : http://qorvanbrief.com</p>
    </div>
    <div class="follow">
      <h4>FOLLOW US ON</h4>
      <ul>
        <li><i></i>Facenote</li>
        <li><i></i>Chirper</li>
        <li><i></i>Snapgram</li>
      </ul>
    </div>
  </div>
</footer>

<div class="abs copyright">Copyright © 2016, All Rights Reserved</div>

</body>
</html>
```